Classic and neutral book cover design

We are looking for a classic and neutral book cover design to be used as the template for a series of books to be published. We are hence looking for a template that will allow us to easily change the title name for all books in this series.
The use of very few colours (black and white is welcome) and few design elements is a big bonus. As a source of inspiration we would like to ask you to view the very simple and
If you think you have a cool idea that can add a twist to the formal classic look don't hesitate. Go for it !
Work will be done for a 30 year old Sweden based cultural non-profit called VĂ©lra (www.velrafoundation.example). We work with the publishing and supporting of post-modern art and literature addressing contemporary topics but are also involved in assisting projects of cultural preservation.
Target Market(s)
The audience is expected to have some form of interest in culture but could range from hobbyist readers to tenure track scholars
Industry/Entity Type
Non-Profit
Requirements
Must have
- General:
- Classic and neutral feel
- Preferably very simple and few shapes
- usage of few colours (black and white is welcome)
Information to be displayed on the cover is:
- Author
- Title
- type of work e.g. play/novel (optional)
- publishing house (in this case "Velra Publishing")
Nice to have
- ideas to prevent it from become boring are of course welcome
Should not have
- - too many colours

```html
<!DOCTYPE html>
<html lang="en">
<head>
<meta charset="utf-8">
<title>Vélra Publishing – Series Cover Template</title>
<link rel="stylesheet" href="https://fonts.googleapis.com/css2?family=Crimson+Text:wght@400;600;700&family=Tinos&display=swap">
<style>
  :root {
    --page-bg: #ffffff;
    --cover-dark: #48484a;
    --cover-mid: #939498;
    --cover-light: #f2efe8;
    --initial-dark: #6f7072;
    --initial-mid: #b3b4b7;
    --initial-light: #d4d4ce;
    --ink-light: #ffffff;
    --ink-dark: #1f1d1d;
    --shadow: rgba(0, 0, 0, 0.28);
  }
  * { margin: 0; padding: 0; box-sizing: border-box; }
  html, body {
    width: 1200px;
    height: 900px;
    overflow: hidden;
    background: var(--page-bg);
  }
  .series {
    position: relative;
    width: 1200px;
    height: 900px;
  }
  .cover {
    position: absolute;
    width: 348px;
    height: 439px;
    overflow: hidden;
    box-shadow: 4px 4px 7px var(--shadow);
    font-family: "Crimson Text", Georgia, serif;
    text-align: center;
  }
  .cover--nonfiction { left: 34px;  top: 193px; background: var(--cover-dark);  color: var(--ink-light); }
  .cover--fiction    { left: 415px; top: 194px; background: var(--cover-mid);   color: var(--ink-light); }
  .cover--poetry     { left: 794px; top: 194px; background: var(--cover-light); color: var(--ink-dark); }

  .cover__initial {
    position: absolute;
    font-family: "Tinos", "Times New Roman", serif;
    font-size: 215px;
    line-height: 1;
    top: 262px;
  }
  .cover--nonfiction .cover__initial { left: 194px; color: var(--initial-dark); }
  .cover--fiction .cover__initial    { left: 243px; top: 268px; color: var(--initial-mid); }
  .cover--poetry .cover__initial     { left: 232px; top: 266px; color: var(--initial-light); }

  .cover__author {
    position: absolute;
    left: 0; right: 0;
    top: 59px;
    font-size: 17px;
    font-weight: 400;
  }
  .cover__title {
    position: absolute;
    left: 0; right: 0;
    font-weight: 600;
  }
  .cover__title--long {
    top: 179px;
    font-size: 22px;
    line-height: 27px;
    letter-spacing: 0.46em;
    padding-left: 0.46em;
  }
  .cover__title--short {
    top: 200px;
    font-size: 38px;
    line-height: 1;
    letter-spacing: 0.5em;
    padding-left: 0.5em;
  }
  .cover__subtitle {
    position: absolute;
    left: 0; right: 0;
    top: 236px;
    font-size: 16px;
    font-weight: 700;
  }
  .cover__imprint {
    position: absolute;
    left: 0; right: 0;
    top: 398px;
    font-size: 16px;
    font-weight: 400;
    letter-spacing: 0.04em;
    color: var(--ink-dark);
  }
  .cover--nonfiction .cover__imprint { color: var(--ink-light); }
</style>
</head>
<body>
<main class="series">
  <article class="cover cover--nonfiction">
    <span class="cover__initial" aria-hidden="true">N</span>
    <p class="cover__author">Étienne Valcourt</p>
    <h1 class="cover__title cover__title--long">ARCHIPELAGO<br>AND CROWN</h1>
    <p class="cover__subtitle">In Northern Diplomacy 1790-1796</p>
    <p class="cover__imprint">VÉLRA</p>
  </article>

  <article class="cover cover--fiction">
    <span class="cover__initial" aria-hidden="true">F</span>
    <p class="cover__author">Étienne Valcourt</p>
    <h1 class="cover__title cover__title--short">TITLE</h1>
    <p class="cover__imprint">VÉLRA</p>
  </article>

  <article class="cover cover--poetry">
    <span class="cover__initial" aria-hidden="true">P</span>
    <p class="cover__author">Étienne Valcourt</p>
    <h1 class="cover__title cover__title--short">TITLE</h1>
    <p class="cover__imprint">VÉLRA</p>
  </article>
</main>
</body>
</html>
```